Vintage poster/postcard for 2011 New Years Eve event with theme 'Velvet Lanterns'

I have had a major change of mind since the last brief due to my original requirements being too specific. I hope this new brief allows more scope for the designers and I am extending the deadline by 7 days.

For the first time my new business 'Larkmoor Galas' is planning an exciting, large scale New Years Eve fundraising event in Hobart Tasmania, Australia. The unique and eclectic theme of the party is 'Velvet Lanterns' (french for contemporary circus). I require a vintage style poster design (similar to a traditional french advertising poster) that can double as a postcard invitation so it must look good on a smaller scale as well.
Updates

Project Deadline Extended
Reason: My original brief was very specific and I now realise very limiting for the designers. I have changed my mind with the look I want for the vintage poster (more along the lines of the traditional french advertising posters of old) and therefore would like to allow designers extra time to submit a design. Thank you. Dena Voss Larkmoor Galas

Target Market(s)

25-50 yr old professionals prepared to pay premium price for a quality, fresh & fun NYE experience while giving to charity.

Industry/Entity Type

Advertising

Requirements
Must have
• - A heading that reads: Larkmoor Galas proudly presents
Velvet Lanterns
- Text that includes: 2011 New Years Eve Extravanaganza Saturday 31st December and find out more at "www.larkmoorgalas.example
- A strip left blank at the bottom to include my business logo and others sponsors
- Classic french vintage poster design
- - Plenty of colour but not too fluro
- Something that looks good enough to be framed or sent to a friend
Should not have
• - Picture of Eiffel Tower or any other specific French references
- Any animals

```html
<!DOCTYPE html>
<html lang="en">
<head>
<meta charset="utf-8">
<title>Velvet Lanterns – New Years Eve Extravaganza</title>
<link rel="stylesheet" href="https://fonts.googleapis.com/css2?family=Oswald:wght@500;600&family=Rye&display=swap">
<style>
  :root {
    --frame-tan: #c39c6e;
    --frame-sand: #bfb49b;
    --red-light: #e83f3f;
    --red-deep: #bc2e3b;
    --teal-light: #014452;
    --teal-deep: #022433;
    --ring: #bfb39a;
    --ink-sand: #c2b8a0;
    --orange: #f29a2e;
    --title-teal: #2aa99b;
    --title-depth: #0e6d66;
    --gold: #f6c04a;
    --scarlet: #d8352f;
    --cream: #fff3e2;
    --ribbon-fold: #c4552a;
  }
  html, body {
    margin: 0;
    padding: 0;
    width: 852px;
    height: 1200px;
    overflow: hidden;
    background: var(--frame-sand);
  }
  .poster {
    display: block;
    width: 852px;
    height: 1200px;
  }
  .sans {
    font-family: "Oswald", "Arial Narrow", sans-serif;
    font-weight: 600;
  }
  .display {
    font-family: "Rye", Georgia, serif;
  }
  .presenter { fill: var(--ink-sand); font-size: 40px; letter-spacing: 1px; }
  .ribbon-text { fill: var(--cream); font-size: 19px; font-weight: 600; }
  .title-line {
    fill: var(--title-teal);
    stroke: var(--orange);
    stroke-width: 2.2px;
    paint-order: stroke;
    font-size: 104px;
  }
  .title-shadow { fill: var(--title-depth); font-size: 104px; }
  .occasion { fill: var(--ink-sand); font-size: 38px; font-weight: 500; }
  .headline-word {
    fill: var(--gold);
    stroke: var(--scarlet);
    stroke-width: 2.4px;
    paint-order: stroke;
    font-size: 52px;
  }
  .event-date { fill: var(--ink-sand); font-size: 40px; font-weight: 500; }
  .more-info { fill: var(--ink-sand); font-size: 19px; font-weight: 500; }
  .web-address { fill: var(--ink-sand); font-size: 13px; font-weight: 600; }
  .dot-row { stroke: var(--orange); stroke-width: 5; stroke-linecap: round; stroke-dasharray: 0 13.5; }
  .rule { stroke: var(--orange); stroke-width: 3; }
</style>
</head>
<body>
<svg class="poster" viewBox="0 0 852 1200" xmlns="http://www.w3.org/2000/svg">
  <defs>
    <linearGradient id="frameGradient" x1="0" y1="0" x2="0" y2="1">
      <stop offset="0" stop-color="var(--frame-tan)"/>
      <stop offset="1" stop-color="var(--frame-sand)"/>
    </linearGradient>
    <pattern id="redStripes" width="116" height="10" patternUnits="userSpaceOnUse" x="26" y="0">
      <rect width="58" height="10" fill="var(--red-light)"/>
      <rect x="58" width="58" height="10" fill="var(--red-deep)"/>
    </pattern>
    <pattern id="tealStripes" width="116" height="10" patternUnits="userSpaceOnUse" x="10" y="0">
      <rect width="58" height="10" fill="var(--teal-light)"/>
      <rect x="58" width="58" height="10" fill="var(--teal-deep)"/>
    </pattern>
  </defs>

  <rect class="frame" width="852" height="1200" fill="url(#frameGradient)"/>
  <rect class="tent-stripes" x="26" y="26" width="800" height="1148" fill="url(#redStripes)"/>

  <ellipse class="oval-ring" cx="426" cy="604" rx="382" ry="520" fill="var(--ring)"/>
  <ellipse class="oval-field" cx="426" cy="604" rx="363" ry="503" fill="url(#tealStripes)"/>

  <text class="sans presenter" x="424" y="182" text-anchor="middle" transform="rotate(2 424 166)">LARKMOOR GALAS</text>

  <g class="ribbon" transform="rotate(-3 424 244)">
    <polygon points="296,240 268,272 318,268 324,258" fill="var(--orange)"/>
    <polygon points="530,236 576,270 522,272 518,258" fill="var(--orange)"/>
    <polygon points="318,258 318,268 330,262" fill="var(--ribbon-fold)"/>
    <rect x="318" y="222" width="210" height="40" fill="var(--orange)" stroke="var(--cream)" stroke-width="1.5"/>
    <text class="sans ribbon-text" x="423" y="249" text-anchor="middle">PROUDLY PRESENTS</text>
  </g>

  <line class="dot-row" x1="131" y1="334" x2="735" y2="334"/>
  <text class="display title-shadow" x="116" y="458" textLength="620" lengthAdjust="spacingAndGlyphs">VELVET</text>
  <text class="display title-line" x="112" y="454" textLength="620" lengthAdjust="spacingAndGlyphs">VELVET</text>
  <text class="display title-shadow" x="123" y="600" textLength="642" lengthAdjust="spacingAndGlyphs">LANTERNS</text>
  <text class="display title-line" x="119" y="596" textLength="642" lengthAdjust="spacingAndGlyphs">LANTERNS</text>
  <line class="dot-row" x1="131" y1="641" x2="773" y2="641"/>

  <text class="sans occasion" x="426" y="697" text-anchor="middle">NEW YEARS EVE</text>
  <text class="display headline-word" x="115" y="776" textLength="626" lengthAdjust="spacingAndGlyphs">EXTRAVAGANZA</text>

  <line class="rule" x1="106" y1="806" x2="737" y2="806"/>
  <line class="rule" x1="145" y1="875" x2="707" y2="875"/>
  <line class="rule" x1="554" y1="806" x2="554" y2="875"/>
  <text class="sans event-date" x="160" y="856" textLength="383" lengthAdjust="spacingAndGlyphs">SATURDAY 31ST DECEMBER 2011</text>
  <text class="sans more-info" x="567" y="838" textLength="136" lengthAdjust="spacingAndGlyphs">FIND OUT MORE AT</text>
  <text class="sans web-address" x="567" y="859" textLength="136" lengthAdjust="spacingAndGlyphs">WWW.LARKMOORGALAS.EXAMPLE</text>
</svg>
</body>
</html>
```